DRUM requires an exciting new business card

New business card required for DRUM. We are a new market research consultancy and want our brand to be approachable and be contemporary/modern, bold, uncomplicated/simple, and use friendly and easy to read fonts.

A draft website front page is attached to give you a feel (the pictures will be improved over the coming days).

The business card will be printed on 600gsm card, full colour both sides. The card is unique in that it allows one of four colours to be placed within the seam of the card (see http://uk.carddeck-example.com/products/deluxe/business-cards.html)

The logo has been designed in yellow on white, white on yellow, yellow on black and black on yellow - please select whichever you feel most appropriate from the attached document (please use the versions with the tagline). I think my preference is yellow on white for the front, and then yellow or black as the dominant colour on the back.

Telephone numbers will be given next week as they are now being finalised.

Thanks

Target Market(s)

Professionals in large corporates, such as Marketing Managers at Orvana, Fizzwell Soda, Hallbrook etc.

Industry/Entity Type

Market Research

Requirements
Must have
• Daniel Wexford QPMR
drum
Level 4, 27 Larkspur St
Brenton Vale
NSW 2188
Tel: 02 XXXX XXXX
Mob: XXXX XXXXXX
Email: daniel@drumresearch-example.com.au
Web: www.drumresearch-example.com.au

```html
<!DOCTYPE html>
<html lang="en">
<head>
<meta charset="utf-8">
<title>DRUM business card</title>
<link rel="stylesheet" href="https://fonts.googleapis.com/css2?family=Montserrat:wght@400;500;700&display=swap">
<style>
  :root {
    --backdrop: #2e2e2e;
    --card-white: #ffffff;
    --card-navy: #263340;
    --brand-yellow: #fdc216;
    --text-light: #ffffff;
  }
  * { margin: 0; padding: 0; box-sizing: border-box; }
  html, body {
    width: 1200px;
    height: 900px;
    overflow: hidden;
    background: var(--backdrop);
    font-family: "Montserrat", sans-serif;
  }
  .stage { position: relative; width: 1200px; height: 900px; }
  .card {
    position: absolute;
    top: 292px;
    width: 481px;
    height: 316px;
    box-shadow: 0 2px 0 rgba(0,0,0,0.5);
  }
  .card--front { left: 105px; background: var(--card-white); }
  .card--back { left: 612px; background: var(--card-navy); color: var(--text-light); }

  .front-name {
    position: absolute;
    left: 50%;
    top: 50%;
    transform: translate(-50%, -50%);
    font-size: 56px;
    font-weight: 700;
    letter-spacing: 8px;
    color: var(--card-navy);
    line-height: 1;
  }

  .back-name {
    position: absolute;
    left: 46px;
    top: 60px;
    font-size: 36px;
    font-weight: 700;
    letter-spacing: 5px;
    color: var(--brand-yellow);
    line-height: 1;
  }

  .person {
    position: absolute;
    left: 200px;
    top: 172px;
  }
  .person__name {
    font-size: 16px;
    font-weight: 500;
    color: var(--brand-yellow);
    letter-spacing: 0.3px;
    line-height: 1;
  }
  .person__title { font-size: 11px; margin-top: 7px; line-height: 1; }

  .address {
    position: absolute;
    left: 46px;
    top: 220px;
    font-size: 11px;
    line-height: 18px;
    font-style: normal;
  }
  .label { color: var(--brand-yellow); }

  .contact {
    position: absolute;
    left: 200px;
    top: 220px;
    font-size: 11px;
    line-height: 18px;
    border-collapse: collapse;
  }
  .contact td { padding: 0; white-space: nowrap; vertical-align: top; }
  .contact .label { width: 48px; }
</style>
</head>
<body>
<main class="stage">
  <section class="card card--front" aria-label="Card front">
    <div class="front-name">DRUM</div>
  </section>

  <section class="card card--back" aria-label="Card back">
    <div class="back-name">DRUM</div>

    <div class="person">
      <div class="person__name">DANIEL WEXFORD</div>
      <div class="person__title">QPMR</div>
    </div>

    <address class="address">
      <div class="label">Address:</div>
      <div>27 Larkspur St</div>
      <div>Brenton Vale</div>
      <div>NSW 2188</div>
    </address>

    <table class="contact">
      <tr><td class="label">Phone:</td><td>02 7400 1186</td></tr>
      <tr><td class="label">Mobile:</td><td>0412 908 337</td></tr>
      <tr><td class="label">Email:</td><td>daniel@drumresearch-example.com.au</td></tr>
      <tr><td class="label">Web:</td><td>www.drumresearch-example.com.au</td></tr>
    </table>
  </section>
</main>
</body>
</html>
```